Radiology Department needs a series of 3 facebook posts - similar design

We need a series of 3 posts for our facebook page, each one presenting the activity of one of 3 physicians.
The main design elements can be the same, the only thing that will change between posts will be the field of activity and name of the physician and the representative image of its activity.
If needed the design elements can be slightly different between posts for better adjustment to the representative images.
You can find as an attachment:
- Manual of institutional identity of the Hospital (Velmor Clinica)
- Our facebook cover page
- Our department video
- The representative images for each post, identified with the name of each physician
- The Institutional identity manual with the logo of "Brisa Medical School" - just for Dr Tomas Brandilo post.
So, each one of the three posts should state the name and field of activity of each physician, including somehow the corresponding representative image, and should have background innovative design elements.
Post 1:
Name of the physician: Prof. Doutor Rui Castelvo
Field of activity: Imagiologia Reumatológica e do Sistema Músculo-Esquelético
Image as an attachment
Post 2:
Name of the physician: Prof.ª Doutora Inês Barroca
Field of activity: Imagiologia Cardíaca
Image as an attachment
Post 3:
Name of the physician: Dr. Tomas Lupo
Field of activity: Tese de Doutoramento em Curso - Identificação da Lesão Cartilagínea Precoce. Com orientação do Prof. Doutor Rui Castelvo e Prof.ª Doutora Inês Sofia Carvalhal.
Image as an attachment
Just for Dr Tomas Lupo, the logo of Brisa Medical School should also be included (please check the corresponding institutional identity manual that was just added in documents).
Updates

Just for Dr Tomas Brandilo, the logo of Brisa Medical School should also be included (please check the corresponding institutional identity manual that was just added in documents).

Please note that we are just looking for 3 facebook POSTS, not facebook cover page, thanks.

Please kindly note that we are looking for facebook POST and NOT facebook cover page.

Target Market(s)

General Population

Industry/Entity Type

Health

Font styles to use
Other font styles liked:
• Check manual of institutional identity and try to approach if appropriate

Requirements
Must have
• Check project description.
Nice to have
• If the designer finds appropriate, the logo of the Hospital would be nice in all the three posts, the most simple one just stating "VelmorClinica" - please check the attached manual of institutional identity

```html
<!DOCTYPE html>
<html lang="pt">
<head>
<meta charset="utf-8">
<title>VelmorClinica – Imagiologia</title>
<link rel="stylesheet" href="https://fonts.googleapis.com/css2?family=Roboto+Condensed:wght@400;700&family=Roboto:wght@700&display=swap">
<style>
  :root {
    --teal-dark: #0b6573;
    --teal-deep: #07505c;
    --yellow: #fcc812;
    --title-yellow: #fdc516;
    --white: #ffffff;
    --black: #000000;
    --brand-teal: #0f6a78;
  }
  html, body { margin: 0; padding: 0; overflow: hidden; }
  .canvas {
    position: relative;
    width: 999px;
    height: 1200px;
    background: var(--white);
    overflow: hidden;
  }
  .backdrop { position: absolute; inset: 0; }
  .backdrop-shape { fill: var(--black); }
  .post {
    position: absolute;
    left: 143px;
    width: 715px;
    height: 272px;
    display: block;
  }
  .post--rheuma { top: 120px; }
  .post--cardiac { top: 438px; }
  .post--thesis { top: 770px; }

  .post-bg { fill: url(#tealField); }
  .brand-band { fill: var(--white); }
  .band-shadow { fill: url(#shadowFade); }
  .accent-yellow { fill: var(--yellow); }
  .accent-dark { fill: var(--teal-dark); }
  .accent-white { fill: var(--white); }
  .corner-teal { fill: var(--teal-dark); }
  .image-frame { fill: var(--black); }
  .name-tag { fill: var(--teal-deep); }
  .brand-dot { fill: var(--brand-teal); }

  .brand-name {
    font-family: "Roboto", Arial, sans-serif;
    font-weight: 700;
    font-size: 66px;
    fill: var(--brand-teal);
  }
  .brand-tagline {
    font-family: "Roboto Condensed", "Arial Narrow", sans-serif;
    font-weight: 400;
    font-size: 29px;
    fill: var(--brand-teal);
  }
  .field-title {
    font-family: "Roboto Condensed", "Arial Narrow", sans-serif;
    font-weight: 700;
    fill: var(--title-yellow);
    paint-order: stroke;
    stroke: rgba(0,0,0,0.35);
    stroke-width: 3px;
  }
  .field-note {
    font-family: "Roboto Condensed", "Arial Narrow", sans-serif;
    font-weight: 400;
    fill: var(--title-yellow);
  }
  .advisors {
    font-family: "Roboto Condensed", "Arial Narrow", sans-serif;
    font-weight: 400;
    font-size: 24px;
    fill: var(--white);
  }
  .physician-name {
    font-family: "Roboto Condensed", "Arial Narrow", sans-serif;
    font-weight: 400;
    font-size: 34px;
    fill: var(--white);
  }
</style>
</head>
<body>
<div class="canvas">

  <svg class="backdrop" width="999" height="1200" viewBox="0 0 999 1200" aria-hidden="true">
    <polygon class="backdrop-shape" points="0,0 209,0 999,960 999,1057 766,1200 0,1200"/>
  </svg>

  <svg width="0" height="0" style="position:absolute" aria-hidden="true">
    <defs>
      <linearGradient id="tealField" x1="0" y1="0" x2="1" y2="1">
        <stop offset="0" stop-color="#0f6f7d"/>
        <stop offset="0.5" stop-color="#168a99"/>
        <stop offset="1" stop-color="#117a88"/>
      </linearGradient>
      <linearGradient id="shadowFade" x1="0" y1="0" x2="1" y2="0">
        <stop offset="0" stop-color="#000" stop-opacity="0.9"/>
        <stop offset="1" stop-color="#000" stop-opacity="0"/>
      </linearGradient>
      <radialGradient id="handsScan" cx="0.6" cy="0.45" r="0.6">
        <stop offset="0" stop-color="#d8776a"/>
        <stop offset="0.55" stop-color="#8a3a33"/>
        <stop offset="1" stop-color="#000"/>
      </radialGradient>
      <radialGradient id="heartScan" cx="0.55" cy="0.45" r="0.5">
        <stop offset="0" stop-color="#8c2a22"/>
        <stop offset="0.6" stop-color="#4a130f"/>
        <stop offset="1" stop-color="#000"/>
      </radialGradient>
      <radialGradient id="kneeScan" cx="0.55" cy="0.5" r="0.65">
        <stop offset="0" stop-color="#0f2fc0"/>
        <stop offset="0.7" stop-color="#1f4ae8"/>
        <stop offset="1" stop-color="#0a1d8a"/>
      </radialGradient>
    </defs>
  </svg>

  <!-- Post 1 -->
  <svg class="post post--rheuma" viewBox="0 0 1252 476">
    <rect class="post-bg" width="1252" height="476"/>
    <polygon class="image-frame" points="922,0 1252,0 1252,476 942,476 697,220"/>
    <polygon role="img" aria-label="Angiografia 3D das duas mãos" fill="url(#handsScan)" points="922,0 1252,0 1252,476 942,476 697,220"/>
    <polygon class="corner-teal" points="1133,0 1252,0 1252,125"/>
    <polygon class="corner-teal" points="1252,330 1252,476 1100,476"/>
    <polygon class="accent-dark" points="867,0 897,0 670,220 885,476 855,476 640,220"/>
    <polygon class="accent-yellow" points="897,0 922,0 697,220 942,476 885,476 670,220"/>
    <polygon class="accent-yellow" points="633,0 867,0 745,116"/>
    <polygon class="accent-white" points="718,476 805,395 885,476"/>
    <polygon class="band-shadow" points="0,198 460,212 0,212"/>
    <polygon class="brand-band" points="0,66 670,66 728,124 653,200 0,200"/>
    <circle class="brand-dot" cx="132" cy="132" r="55"/>
    <text class="brand-name" x="198" y="144">VelmorClinica</text>
    <text class="brand-tagline" x="199" y="180">Construímos relações de confiança</text>
    <text class="field-title" x="82" y="290" font-size="54">Imagiologia Reumatológica</text>
    <text class="field-title" x="82" y="340" font-size="44">e do Sistema Músculo-Esquelético</text>
    <polygon class="name-tag" points="370,373 800,373 800,413 405,413"/>
    <text class="physician-name" x="405" y="404">Prof. Doutor Rui Castelvo</text>
  </svg>

  <!-- Post 2 -->
  <svg class="post post--cardiac" viewBox="0 0 1252 476">
    <rect class="post-bg" width="1252" height="476"/>
    <polygon class="image-frame" points="922,0 1252,0 1252,476 942,476 697,220"/>
    <ellipse role="img" aria-label="Reconstrução 3D do coração e artérias coronárias" fill="url(#heartScan)" cx="1000" cy="210" rx="160" ry="150"/>
    <polygon class="corner-teal" points="1133,0 1252,0 1252,125"/>
    <polygon class="corner-teal" points="1252,330 1252,476 1100,476"/>
    <polygon class="accent-dark" points="867,0 897,0 670,220 885,476 855,476 640,220"/>
    <polygon class="accent-yellow" points="897,0 922,0 697,220 942,476 885,476 670,220"/>
    <polygon class="accent-yellow" points="633,0 867,0 745,116"/>
    <polygon class="accent-white" points="718,476 805,395 885,476"/>
    <polygon class="band-shadow" points="0,198 460,212 0,212"/>
    <polygon class="brand-band" points="0,66 670,66 728,124 653,200 0,200"/>
    <circle class="brand-dot" cx="132" cy="132" r="55"/>
    <text class="brand-name" x="198" y="144">VelmorClinica</text>
    <text class="brand-tagline" x="199" y="180">Construímos relações de confiança</text>
    <text class="field-title" x="133" y="341" font-size="64">Imagiologia Cardíaca</text>
    <polygon class="name-tag" points="370,373 800,373 800,413 405,413"/>
    <text class="physician-name" x="405" y="404">Prof.ª Doutora Inês Barroca</text>
  </svg>

  <!-- Post 3 -->
  <svg class="post post--thesis" viewBox="0 0 1252 476">
    <rect class="post-bg" width="1252" height="476"/>
    <polygon class="image-frame" points="922,0 1252,0 1252,476 942,476 697,220"/>
    <polygon role="img" aria-label="Mapa de ressonância magnética da cartilagem do joelho" fill="url(#kneeScan)" points="922,0 1130,0 1252,80 1252,310 1080,476 980,476 745,215"/>
    <polygon class="corner-teal" points="1133,0 1252,0 1252,125"/>
    <polygon class="corner-teal" points="1252,330 1252,476 1100,476"/>
    <polygon class="accent-dark" points="867,0 897,0 670,220 885,476 855,476 640,220"/>
    <polygon class="accent-yellow" points="897,0 922,0 697,220 942,476 885,476 670,220"/>
    <polygon class="accent-yellow" points="633,0 867,0 745,116"/>
    <polygon class="accent-white" points="718,476 805,395 885,476"/>
    <polygon class="band-shadow" points="0,198 460,212 0,212"/>
    <polygon class="brand-band" points="0,66 670,66 728,124 653,200 0,200"/>
    <circle class="brand-dot" cx="132" cy="132" r="55"/>
    <text class="brand-name" x="198" y="144">VelmorClinica</text>
    <text class="brand-tagline" x="199" y="180">Construímos relações de confiança</text>
    <text class="field-title" x="80" y="277" font-size="44">Tese de Doutoramento em Curso -</text>
    <text class="field-title" x="80" y="316" font-size="33">Identificação da Lesão Cartilagínea Precoce.Com</text>
    <text class="field-note" x="80" y="352" font-size="34">orientação do</text>
    <text class="advisors" x="80" y="381">Prof. Doutor Rui Castelvo e</text>
    <text class="advisors" x="80" y="408">Prof.ª Doutora Inês Sofia Carvalhal.</text>
    <polygon class="name-tag" points="482,373 800,373 800,413 517,413"/>
    <text class="physician-name" x="535" y="404">Dr. Tomas Lupo</text>
  </svg>

</div>
</body>
</html>
```